Business Card Design for Loft Pictures

Hi we need a business card designed for a new aerial photography business we have started, we use UAV Drones to take photos for corporate, events, real estate, local government etc , the business name is Loft Pictures Australia, we have a facebook page that might help you come up with some designs - https://www.facebook.com/loftpicturesaustralia

We need to have and editable AI file so that we can use different names and contact details. details for one of the cards as follow:

Ned Harrow
phone: 03 5521 4736
Mobile: 0431 957 284
email: ned@loftpicturez.example
web: www.loftpictures.example

have now changed: Designer Payment:Committed

Target Market(s)

We are a Aerial Photography business using Drones and UAV

Industry/Entity Type

Business

Logo Text

Loft Pictures Australia

Requirements
Must have
• Colors to match logo and be part of Loft Pictures Brand

```html
<!DOCTYPE html>
<html lang="en">
<head>
<meta charset="utf-8">
<title>Loft Pictures Australia – Business Card</title>
<link rel="stylesheet" href="https://fonts.googleapis.com/css2?family=Michroma&display=swap">
<style>
  :root {
    --page: #ffffff;
    --sky-light: #cfe9fb;
    --sky-mid: #5fa6dc;
    --ground-deep: #0a4f93;
    --ground-dark: #083f7c;
    --accent: #1ec0ef;
    --white: #ffffff;
    --shadow: rgba(0, 0, 0, 0.35);
  }
  html, body {
    margin: 0;
    width: 1200px;
    height: 1000px;
    overflow: hidden;
    background: var(--page);
    font-family: "Michroma", sans-serif;
  }
  .canvas { position: relative; width: 1200px; height: 1000px; }
  .card {
    position: absolute;
    left: 231px;
    width: 724px;
    height: 414px;
    overflow: hidden;
    box-shadow: 4px 5px 6px var(--shadow);
  }
  .card--front { top: 31px; }
  .card--back { top: 545px; background: var(--white); }
  .card svg { position: absolute; left: 0; top: 0; }

  .brand {
    position: absolute;
    text-align: center;
    text-transform: uppercase;
    line-height: 1;
  }
  .brand__name { display: block; font-size: 40px; letter-spacing: 1px; }
  .brand__region { display: block; font-size: 15px; letter-spacing: 7px; margin-top: 14px; }
  .card--front .brand { left: 162px; top: 164px; width: 400px; color: var(--white); }
  .card--back .brand { left: 454px; top: 157px; width: 240px; color: var(--accent); }
  .card--back .brand__name { font-size: 30px; }
  .card--back .brand__name + .brand__name { margin-top: 6px; }
  .card--front .brand__name + .brand__name { margin-top: 8px; }

  .contact {
    position: absolute;
    left: 35px;
    top: 158px;
    color: var(--white);
    text-transform: uppercase;
  }
  .contact__name {
    font-size: 19px;
    letter-spacing: 2px;
    padding-bottom: 6px;
    border-bottom: 1px solid var(--white);
    width: 212px;
    margin: 0 0 7px;
    font-weight: normal;
  }
  .contact__line { font-size: 10.5px; letter-spacing: 0.5px; line-height: 20px; margin: 0; white-space: nowrap; }
  .contact__web { text-decoration: underline; }
</style>
</head>
<body>
<div class="canvas">

  <section class="card card--front">
    <svg width="724" height="414" viewBox="0 0 724 414">
      <defs>
        <linearGradient id="frontPhoto" x1="0" y1="0" x2="0" y2="1">
          <stop offset="0" stop-color="var(--sky-light)"/>
          <stop offset="0.25" stop-color="var(--sky-mid)"/>
          <stop offset="0.4" stop-color="var(--ground-deep)"/>
          <stop offset="1" stop-color="var(--ground-dark)"/>
        </linearGradient>
      </defs>
      <rect width="724" height="414" fill="url(#frontPhoto)" role="img" aria-label="Aerial photograph of a city skyline over a lake and parkland, tinted blue"/>
      <g class="focus-points" fill="none" stroke="var(--white)" stroke-width="3">
        <rect x="340" y="35" width="45" height="33" rx="5"/>
        <rect x="174" y="100" width="33" height="45" rx="5"/>
        <rect x="518" y="100" width="33" height="45" rx="5"/>
        <rect x="56" y="184" width="33" height="45" rx="5"/>
        <rect x="635" y="184" width="33" height="45" rx="5"/>
        <rect x="174" y="267" width="33" height="45" rx="5"/>
        <rect x="518" y="267" width="33" height="45" rx="5"/>
        <rect x="340" y="347" width="45" height="33" rx="5"/>
      </g>
    </svg>
    <div class="brand">
      <span class="brand__name">Loft</span>
      <span class="brand__name">Pictures</span>
      <span class="brand__region">Australia</span>
    </div>
  </section>

  <section class="card card--back">
    <svg width="724" height="414" viewBox="0 0 724 414">
      <defs>
        <linearGradient id="backPhoto" x1="0" y1="0" x2="0" y2="1">
          <stop offset="0" stop-color="var(--sky-light)"/>
          <stop offset="0.25" stop-color="var(--sky-mid)"/>
          <stop offset="0.4" stop-color="var(--ground-deep)"/>
          <stop offset="1" stop-color="var(--ground-dark)"/>
        </linearGradient>
      </defs>
      <rect width="724" height="414" fill="url(#backPhoto)" role="img" aria-label="Aerial photograph of a city skyline over a lake and parkland, tinted blue"/>
      <polygon class="chevron-band" points="469,0 724,0 724,414 484,414 276,207" fill="var(--accent)"/>
      <polygon class="brand-panel" points="554,0 724,0 724,414 569,414 364,207" fill="var(--white)"/>
    </svg>
    <div class="contact">
      <h1 class="contact__name">Ned Harrow</h1>
      <p class="contact__line">Phone: 03 5521 4736</p>
      <p class="contact__line">Mobile: 0431 957 284</p>
      <p class="contact__line">Email: ned@loftpicturez.example</p>
      <p class="contact__line">Web: <span class="contact__web">www.loftpictures.example</span></p>
    </div>
    <div class="brand">
      <span class="brand__name">Loft</span>
      <span class="brand__name">Pictures</span>
      <span class="brand__region">Australia</span>
    </div>
  </section>

</div>
</body>
</html>
```